****Business Card Design for Cormorant Ridge. Design based around attached logo/company name

I’m looking for business card design for my company Cormorant Ridge Holdings,LLC. Design should be professional, sharp and minimal. Outside of the attached logos, greyscale colors for remainder of cards. My thoughts are two-sided card with attached logo on one side and my info on the other but open to one-sided as well with right design.
Target Market(s)
Real estate professionals including banks, private investors, property owners, developers, commercial tenants like Brewloft, Grocana or Tandberry’s.
Industry/Entity Type
Commercial real estate development and investments.
Contact Information for Business Card
Name, title, email, phone #’s, web address and physical address
Font styles to use
Other font styles liked:
- Helvetica, Garamond, etc
Colors
Designer to choose only greyscale colors for use in the design.
Requirements
Must have
- Attached logo first or second options.
Nice to have
- Two sided card with logo on one side. Attached Logo/company name can be laid out any way that flows as long as it’s legible.name
Should not have
- No loud colors. ***Please do not include logo, I have removed the company design with a logo image.

```html
<!DOCTYPE html>
<html lang="en">
<head>
<meta charset="utf-8">
<title>Cormorant Ridge Holdings – Business Card</title>
<link href="https://fonts.googleapis.com/css2?family=Libre+Baskerville:wght@700&family=Arimo:wght@400&display=swap" rel="stylesheet">
<style>
  :root {
    --backdrop: #2b2b2d;
    --card: #ffffff;
    --slate: #5b6475;
    --ink-grey: #8a8a8a;
    --icon: #5b6475;
    --panel-text: #ffffff;
  }
  * { box-sizing: border-box; margin: 0; padding: 0; }
  html, body { width: 1200px; height: 901px; overflow: hidden; }
  body { background: var(--backdrop); position: relative; }

  .card {
    position: absolute;
    left: 80px; top: 153px;
    width: 1040px; height: 594px;
    background: var(--card);
  }
  .brand-panel {
    position: absolute;
    left: 44px; top: 140px;
    width: 500px; bottom: 0;
    background: var(--slate);
  }
  .company-name {
    position: absolute;
    left: 24px; right: 24px; top: 120px;
    text-align: center;
    font-family: Arimo, Helvetica, Arial, sans-serif;
    font-weight: 400;
    font-size: 26px;
    line-height: 1.3;
    color: var(--panel-text);
  }

  .contact {
    position: absolute;
    left: 588px; top: 222px;
    font-family: Arimo, Helvetica, Arial, sans-serif;
    color: var(--ink-grey);
  }
  .person-name {
    font-family: "Libre Baskerville", serif;
    font-weight: 700;
    font-size: 30px;
    color: var(--slate);
    text-transform: uppercase;
    letter-spacing: 1px;
  }
  .person-title { font-size: 21px; margin-top: 4px; }
  .address { font-size: 21px; line-height: 1.3; margin-top: 26px; }
  .channels { list-style: none; margin-top: 22px; font-size: 21px; }
  .channels li { display: flex; align-items: center; gap: 14px; height: 34px; }
  .channels svg { width: 18px; height: 18px; flex: none; fill: var(--icon); }
</style>
</head>
<body>
  <section class="card">
    <div class="brand-panel">
      <p class="company-name">Cormorant Ridge Holdings,LLC</p>
    </div>

    <div class="contact">
      <h1 class="person-name">Daniel Voss</h1>
      <p class="person-title">Founder/CEO</p>
      <p class="address">8474 Street Address Name<br>Counter name AB 7841</p>
      <ul class="channels">
        <li>
          <svg viewBox="0 0 24 24" aria-hidden="true"><path d="M6.6 10.8c1.4 2.8 3.8 5.1 6.6 6.6l2.2-2.2c.3-.3.7-.4 1-.2 1.1.4 2.3.6 3.6.6.6 0 1 .4 1 1V20c0 .6-.4 1-1 1C10.6 21 3 13.4 3 4c0-.6.4-1 1-1h3.5c.6 0 1 .4 1 1 0 1.3.2 2.5.6 3.6.1.3 0 .7-.2 1l-2.3 2.2z"/></svg>
          <span>(123)-555-0148</span>
        </li>
        <li>
          <svg viewBox="0 0 24 24" aria-hidden="true"><path d="M2 5h20v14H2z M2 5l10 8 10-8" fill="none" stroke="#5b6475" stroke-width="2"/><path d="M2 5h20l-10 8z"/></svg>
          <span>info@cormorantridge.com</span>
        </li>
        <li>
          <svg viewBox="0 0 24 24" aria-hidden="true"><circle cx="12" cy="12" r="10"/><path d="M2 12h20M12 2c3 3 3 17 0 20M12 2c-3 3-3 17 0 20" fill="none" stroke="#ffffff" stroke-width="1.4"/></svg>
          <span>www.cormorantridge.com</span>
        </li>
      </ul>
    </div>
  </section>
</body>
</html>
```